Business card - mobile service

O KiraTel is a mobile family safety service based on tablets and smartphones.
The business card must have:
BASIC INFO
Company Logo
Name
Position / Job Title: Co-founder
Mobile Phone Number: +55 (11) 5080 6172
Land Line: +55 (11) 9087 614352
Email Address: name@kiratel-example.com
Web Site URL: www.kiratel-example.com
PROMOTIONAL INFO
Try KiraTel free Today!
Your personal promo code: xxxx-2222-uuuu-7777-1234
Promo code text explanation with the instructions about the trial offer
Updates
Dears,
One more must have: the KiraTel slogan:
Industry/Entity Type
Safety
Look and feel
Each slider illustrates characteristics of the customer's brand and the style your logo design should communicate.

```html
<!DOCTYPE html>
<html lang="en">
<head>
<meta charset="utf-8">
<title>KiraTel business card</title>
<link rel="stylesheet" href="https://fonts.googleapis.com/css2?family=Questrial&display=swap">
<style>
  :root {
    --sky: #3ab3e8;
    --sky-deep: #1796d6;
    --sun: #f7c318;
    --ink-blue: #1f9fdc;
    --white: #ffffff;
    --paper: #fbfcfd;
    --stage: #e9ecef;
    --muted: #5f8aa6;
  }
  * { box-sizing: border-box; margin: 0; padding: 0; }
  html, body { width: 1200px; height: 871px; overflow: hidden; }
  body {
    background: var(--stage);
    font-family: "Questrial", "Century Gothic", sans-serif;
    display: flex;
    flex-direction: column;
    align-items: center;
    justify-content: center;
    gap: 30px;
  }
  .card {
    position: relative;
    width: 700px;
    height: 400px;
    overflow: hidden;
    box-shadow: 0 4px 14px rgba(0,0,0,0.15);
  }
  .band {
    position: absolute;
    left: 0; right: 0; bottom: 0;
    height: 62px;
    background: var(--sun);
  }

  /* Front */
  .card-front {
    background: linear-gradient(160deg, var(--sky) 0%, var(--sky-deep) 100%);
    color: var(--white);
  }
  .brand {
    position: absolute;
    top: 92px;
    left: 0; right: 0;
    text-align: center;
    font-size: 78px;
    letter-spacing: 1px;
    line-height: 1;
    color: var(--white);
  }
  .slogan {
    position: absolute;
    top: 190px;
    left: 0; right: 0;
    text-align: center;
    font-size: 34px;
    font-weight: 700;
    color: var(--sun);
  }
  .person {
    position: absolute;
    top: 262px;
    left: 0; right: 0;
    text-align: center;
    font-size: 21px;
  }
  .person .divider { margin: 0 8px; }
  .contacts {
    position: absolute;
    top: 300px;
    left: 30px; right: 30px;
    display: flex;
    justify-content: space-between;
    font-size: 15px;
  }
  .contact { display: flex; align-items: center; gap: 7px; }
  .icon { width: 18px; height: 18px; flex: none; }
  .website {
    position: absolute;
    left: 0; right: 0; bottom: 0;
    height: 62px;
    line-height: 62px;
    text-align: center;
    font-size: 30px;
    color: var(--white);
  }

  /* Back */
  .card-back { background: var(--paper); color: var(--ink-blue); }
  .card-back .brand {
    top: 70px;
    left: 40px; right: auto;
    text-align: left;
    font-size: 66px;
    color: var(--ink-blue);
  }
  .card-back .slogan {
    top: 150px;
    left: 40px; right: auto;
    text-align: left;
    font-size: 24px;
    color: var(--sun);
  }
  .offer {
    position: absolute;
    top: 78px;
    right: 40px;
    width: 310px;
    text-align: right;
  }
  .offer-title { font-size: 24px; font-weight: 700; }
  .offer-title .accent { color: var(--sun); }
  .offer-note { margin-top: 12px; font-size: 14px; line-height: 1.5; color: var(--muted); }
  .promo {
    position: absolute;
    left: 40px;
    bottom: 84px;
    font-size: 16px;
    line-height: 1.5;
  }
  .promo-code { font-size: 20px; font-weight: 700; letter-spacing: 1px; }
</style>
</head>
<body>

  <section class="card card-front">
    <div class="brand">KiraTel</div>
    <div class="slogan">Keeping Every Home Close</div>
    <div class="person">Marina Costa<span class="divider">|</span>Co-founder</div>
    <div class="contacts">
      <div class="contact">
        <svg class="icon" viewBox="0 0 18 18" aria-hidden="true">
          <rect width="18" height="18" rx="3" fill="#f7c318"/>
          <rect x="6" y="3" width="6" height="12" rx="1" fill="none" stroke="#fff" stroke-width="1.5"/>
          <circle cx="9" cy="13" r="0.8" fill="#fff"/>
        </svg>
        <span>+55 (11) 5080 6172</span>
      </div>
      <div class="contact">
        <svg class="icon" viewBox="0 0 18 18" aria-hidden="true">
          <rect width="18" height="18" rx="3" fill="#f7c318"/>
          <path d="M5 4.5c1-.8 1.8-.4 2.3.6l.6 1.3c.3.7 0 1.2-.6 1.6.5 1.3 1.5 2.3 2.8 2.8.4-.6.9-.9 1.6-.6l1.3.6c1 .5 1.4 1.3.6 2.3-2.5 2.6-9.8-4.6-8.6-8.6z" fill="#fff"/>
        </svg>
        <span>+55 (11) 9087 614352</span>
      </div>
      <div class="contact">
        <svg class="icon" viewBox="0 0 18 18" aria-hidden="true">
          <rect width="18" height="18" rx="3" fill="#f7c318"/>
          <rect x="3.5" y="5" width="11" height="8" fill="none" stroke="#fff" stroke-width="1.4"/>
          <path d="M3.5 5l5.5 4.5L14.5 5" fill="none" stroke="#fff" stroke-width="1.4"/>
        </svg>
        <span>NAME@KIRATEL-EXAMPLE.COM</span>
      </div>
    </div>
    <div class="band"></div>
    <div class="website">www.kiratel-example.com</div>
  </section>

  <section class="card card-back">
    <div class="brand">KiraTel</div>
    <div class="slogan">Keeping Every Home Close</div>
    <div class="offer">
      <div class="offer-title">Try KiraTel <span class="accent">FREE</span> Today!</div>
      <p class="offer-note">Enter this code in the app to start<br>your free 30-day trial.</p>
    </div>
    <div class="promo">
      <div>Your personal promo code:</div>
      <div class="promo-code">xxxx-2222-uuuu-7777-1234</div>
    </div>
    <div class="band"></div>
  </section>

</body>
</html>
```